Print and E-book Personal Injury Front and Back Book Cover

I need a book cover for a personal injury law firm book titled "Beyond the Broken Road" with the subtitle "Making Sense of Accident Claims." The book cover should have an image. This isas a lead generation book designed to be give to potential clients to have them sign as new clients.

Target Market(s)

Potential New Clients Looking For a Personal Injury Attorney

Industry/Entity Type

Legal

Requirements
Must have
• Title and some type of image or images

```html
<!DOCTYPE html>
<html lang="en">
<head>
<meta charset="utf-8">
<title>Beyond the Broken Road – Book Cover</title>
<link rel="stylesheet" href="https://fonts.googleapis.com/css2?family=Cinzel:wght@600;700&family=Open+Sans:wght@400&display=swap">
<style>
  :root {
    --page-bg: #ffffff;
    --cover-dark: #2e2724;
    --cover-mid: #4a3e38;
    --cover-light: #65564d;
    --silver-hi: #ffffff;
    --silver-mid: #c9c9c9;
    --silver-lo: #8a8a8a;
    --text-light: #ece6e1;
    --photo-a: #6b5a4e;
    --photo-b: #3a2a24;
    --photo-c: #8a6a3c;
  }
  * { margin: 0; padding: 0; box-sizing: border-box; }
  html, body { width: 1200px; height: 386px; overflow: hidden; background: var(--page-bg); }
  .stage { position: relative; width: 1200px; height: 386px; }
  .wrap {
    position: absolute; left: 318px; top: 0; width: 564px; height: 386px;
    display: flex;
  }
  .back {
    width: 258px; height: 100%;
    background: radial-gradient(ellipse at 50% 12%, var(--cover-light) 0%, var(--cover-mid) 45%, var(--cover-dark) 100%);
    text-align: center; padding-top: 18px;
  }
  .spine {
    width: 48px; height: 100%;
    background: linear-gradient(90deg, var(--cover-dark), var(--cover-mid) 50%, var(--cover-dark));
    position: relative;
  }
  .front {
    width: 258px; height: 100%; position: relative;
    background: linear-gradient(180deg, var(--cover-mid) 0%, var(--cover-dark) 100%);
    text-align: center;
  }
  .title {
    font-family: "Cinzel", serif; font-weight: 700; line-height: 0.92;
    background: linear-gradient(180deg, var(--silver-hi) 0%, var(--silver-mid) 45%, var(--silver-lo) 55%, var(--silver-hi) 100%);
    -webkit-background-clip: text; background-clip: text; color: transparent;
    filter: drop-shadow(0 1px 1px rgba(0,0,0,0.7));
  }
  .title span { display: block; }
  .back .title .line-a { font-size: 19px; }
  .back .title .line-b { font-size: 31px; }
  .back .title .line-c { font-size: 22px; }
  .front .title { margin-top: 8px; }
  .front .title .line-a { font-size: 26px; }
  .front .title .line-b { font-size: 44px; }
  .front .title .line-c { font-size: 31px; }
  .subtitle {
    font-family: "Cinzel", serif; font-weight: 700; color: var(--text-light);
    font-size: 8.5px; letter-spacing: 0.1px;
  }
  .back .subtitle { margin-top: 8px; }
  .front .subtitle { padding-top: 22px; }
  .blurb {
    font-family: "Open Sans", sans-serif; color: var(--text-light);
    font-size: 6.4px; line-height: 10.2px; text-align: justify; text-align-last: center;
    padding: 0 19px; margin-top: 10px;
  }
  .blurb p + p { margin-top: 10px; }
  .cover-photo {
    position: absolute; left: 0; top: 162px; width: 258px; height: 182px;
    background:
      radial-gradient(ellipse at 42% 78%, var(--photo-b) 0%, transparent 45%),
      radial-gradient(ellipse at 80% 40%, var(--photo-c) 0%, transparent 35%),
      linear-gradient(180deg, var(--photo-a), var(--photo-b));
  }
  .author {
    font-family: "Cinzel", serif; font-weight: 600; color: var(--text-light);
    font-size: 14px; letter-spacing: 0.3px;
  }
  .front .author { position: absolute; left: 0; right: 0; top: 353px; }
  .spine-text {
    position: absolute; left: 50%; transform-origin: 0 0;
    font-family: "Cinzel", serif; font-weight: 600; color: var(--text-light);
    white-space: nowrap;
  }
  .spine-title { top: 22px; transform: rotate(90deg) translateY(-50%); font-size: 14.5px; }
  .spine-author { top: 279px; transform: rotate(90deg) translateY(-50%); font-size: 12px; }
</style>
</head>
<body>
<div class="stage">
  <div class="wrap">
    <section class="back">
      <h2 class="title"><span class="line-a">BEYOND THE</span><span class="line-b">BROKEN</span><span class="line-c">ROAD</span></h2>
      <p class="subtitle">MAKING SENSE OF ACCIDENT CLAIMS</p>
      <div class="blurb">
        <p>Lorem ipsum dolor sit amet, consectetur adipiscing elit, sed do eiusmod tempor incididunt ut labore et dolore magna aliqua. Quis ipsum suspendisse ultrices gravida. Risus commodo viverra maecenas accumsan lacus vel facilisis. Lorem ipsum dolor sit amet, consectetur adipiscing elit, sed do eiusmod tempor incididunt ut labore et dolore magna aliqua. Quis ipsum suspendisse ultrices gravida. Risus commodo viverra maecenas accumsan lacus vel facilisis.</p>
        <p>Lorem ipsum dolor sit amet, consectetur adipiscing elit, sed do eiusmod tempor incididunt ut labore et dolore magna aliqua. Quis ipsum suspendisse ultrices gravida. Risus commodo viverra maecenas accumsan lacus vel facilisis. Lorem ipsum dolor sit amet, consectetur adipiscing elit, sed do eiusmod tempor incididunt ut labore et dolore magna aliqua. Quis ipsum suspendisse ultrices gravida. Risus commodo viverra maecenas accumsan lacus vel facilisis.</p>
        <p>Lorem ipsum dolor sit amet, consectetur adipiscing elit, sed do eiusmod tempor incididunt ut labore et dolore magna aliqua. Quis ipsum suspendisse ultrices gravida. Risus commodo viverra maecenas accumsan lacus vel facilisis. Lorem ipsum dolor sit amet, consectetur adipiscing elit, sed do eiusmod tempor incididunt ut labore et dolore magna aliqua. Quis ipsum suspendisse ultrices gravida. Risus commodo viverra maecenas accumsan lacus vel facilisis.</p>
      </div>
    </section>
    <section class="spine">
      <span class="spine-text spine-title">BEYOND THE BROKEN ROAD</span>
      <span class="spine-text spine-author">AUTHOR NAME</span>
    </section>
    <section class="front">
      <p class="subtitle">MAKING SENSE OF ACCIDENT CLAIMS</p>
      <h1 class="title"><span class="line-a">BEYOND THE</span><span class="line-b">BROKEN</span><span class="line-c">ROAD</span></h1>
      <div class="cover-photo" role="img" aria-label="Photo of a wooden judge's gavel on its block beside law books and brass scales of justice on a dark desk"></div>
      <p class="author">AUTHOR NAME</p>
    </section>
  </div>
</div>
</body>
</html>
```